Business Card Design

I need a business card and logo for a new company based in Manhattan, Kansas called "Bright Ladder, LLC". I am a project management consultant. I specialize in laying the foundation for businesses and business owners to get their projects on track. Think of it as if you were wanting to go from coast to coast on a train. Before you can jump on the train and sell tickets, you have to design the path the train will take, acquire the land, clear the trees, level the ground, prepare the base for the track, lay the track and finally place the train on the track (That's what I do with my clients). Once the train is on the track and I've provided them with the operations manual, then they and their managers get to drive the train. I don't have color preferences. The final design should communicate a clear direction or path to growing the customer's business.
Updates

Since I am in need of a logo as well, I have also created a logo design project that will work in conjunction with this project.

Project Deadline Extended
Reason: Accepted a company logo this afternoon that I would like to have cards designed around. Sorry for jumping the gun and posting both projects at the same time.

Industry/Entity Type

Business

Contact Information for Business Card

Owner: Dale Perrin. Business Name: Bright Ladder, LLC. Business Address: 4871 Maplewood Lane, Larkfield, OR, 97999. Business Phone Number: 555-640-1759. Business Email: dale@brightladderllc.example

```html
<!DOCTYPE html>
<html lang="en">
<head>
<meta charset="utf-8">
<title>Bright Ladder, LLC — Business Card</title>
<link rel="stylesheet" href="https://fonts.googleapis.com/css2?family=Lato:wght@400;700&display=swap">
<style>
  :root {
    --backdrop: #656565;
    --card: #ffffff;
    --brand-blue: #2a6ab5;
    --name-blue: #1d4e9e;
    --text-blue: #1f4f9c;
    --muted-grey: #8a8a8a;
    --rule-blue: #3f6fc0;
  }
  * { box-sizing: border-box; margin: 0; padding: 0; }
  html, body {
    width: 992px;
    height: 1200px;
    overflow: hidden;
    background: var(--backdrop);
    font-family: "Lato", Arial, sans-serif;
  }
  .card {
    position: absolute;
    left: 68px;
    top: 378px;
    width: 869px;
    height: 494px;
    background: var(--card);
    border-radius: 52px;
  }
  .brand {
    position: absolute;
    left: 0;
    width: 432px;
    top: 196px;
    text-align: center;
  }
  .brand-dot {
    display: block;
    width: 70px;
    height: 70px;
    margin: 0 auto 8px;
    border-radius: 50%;
    background: var(--brand-blue);
  }
  .brand-name {
    font-size: 31px;
    font-weight: 700;
    font-variant: small-caps;
    letter-spacing: 1.5px;
    color: var(--brand-blue);
    line-height: 1.1;
  }
  .divider {
    position: absolute;
    left: 432px;
    top: 72px;
    width: 2px;
    height: 350px;
    background: var(--rule-blue);
  }
  .person {
    position: absolute;
    left: 511px;
    top: 96px;
  }
  .person-name {
    font-size: 27px;
    font-weight: 700;
    color: var(--name-blue);
    line-height: 34px;
  }
  .person-role {
    font-size: 19px;
    color: var(--muted-grey);
    line-height: 24px;
  }
  .contact {
    position: absolute;
    left: 470px;
    top: 245px;
    list-style: none;
  }
  .contact li {
    display: flex;
    align-items: flex-start;
    font-size: 19.5px;
    color: var(--text-blue);
    line-height: 25px;
    margin-bottom: 21px;
  }
  .contact svg {
    width: 24px;
    height: 20px;
    margin-right: 18px;
    margin-top: 2px;
    flex-shrink: 0;
    fill: var(--text-blue);
  }
</style>
</head>
<body>
  <div class="card">
    <div class="brand">
      <span class="brand-dot"></span>
      <div class="brand-name">Bright Ladder, LLC</div>
    </div>

    <div class="divider"></div>

    <div class="person">
      <div class="person-name">DALE PERRIN</div>
      <div class="person-role">Owner</div>
    </div>

    <ul class="contact">
      <li>
        <svg viewBox="0 0 24 20" aria-hidden="true">
          <path d="M2 7c0-3 5-5 10-5s10 2 10 5v2h-5V7H7v2H2z"/>
          <rect x="5" y="10" width="14" height="9" rx="1.5"/>
        </svg>
        555-640-1759
      </li>
      <li>
        <svg viewBox="0 0 24 20" aria-hidden="true">
          <path d="M1 2h22v16H1z M3 4v1l9 7 9-7V4z M3 7.5V16h18V7.5l-9 7z" fill-rule="evenodd"/>
        </svg>
        dale@brightladderllc.example
      </li>
      <li>
        <svg viewBox="0 0 24 20" aria-hidden="true">
          <path d="M12 1 1 10h3v9h6v-6h4v6h6v-9h3z"/>
        </svg>
        <span>4871 Maplewood Lane, Larkfield,<br>OR, 97999</span>
      </li>
    </ul>
  </div>
</body>
</html>
```